Brimvale Foods Packing Ace the Day

5 Principals for all the team to follow by!

Please can you convert the Ace the day "screenshot 2024-09-08" image into something that has a similair look and feel to the Vision and Values style?

```html
<!DOCTYPE html>
<html lang="en">
<head>
<meta charset="utf-8">
<title>Brimvale Foods Packing – Ace the Day: 5 Principals</title>
<link href="https://fonts.googleapis.com/css2?family=Montserrat:wght@500;700;800&display=swap" rel="stylesheet">
<style>
  :root {
    --paper: #ffffff;
    --brand-red: #c8222a;
    --hs-yellow: #d5bf56;
    --intro-green: #6cbd4a;
    --gmp-teal: #569fab;
    --team-orange: #d05a27;
    --plan-red: #b92227;
    --process-navy: #22252f;
    --text-light: #ffffff;
    --rule: rgba(255, 255, 255, 0.75);
    --ghost: rgba(255, 255, 255, 0.10);
  }
  * { box-sizing: border-box; margin: 0; padding: 0; }
  html, body {
    width: 1200px;
    height: 800px;
    overflow: hidden;
    background: var(--paper);
    font-family: "Montserrat", Arial, sans-serif;
  }
  .board {
    position: relative;
    width: 1200px;
    height: 800px;
    background: var(--paper);
  }

  /* Brand block, set vertically on the left */
  .brand {
    position: absolute;
    left: 50px;
    top: 69px;
    width: 130px;
    height: 620px;
  }
  .brand-name {
    position: absolute;
    left: 50%;
    top: 50%;
    transform: translate(-50%, -50%) rotate(-90deg);
    white-space: nowrap;
    color: var(--brand-red);
    font-weight: 800;
    font-size: 56px;
    letter-spacing: 1px;
    text-transform: uppercase;
    line-height: 1;
  }
  .brand-name small {
    display: block;
    text-align: center;
    font-size: 26px;
    letter-spacing: 22px;
    margin-top: 10px;
  }

  /* Principles grid */
  .principles {
    position: absolute;
    left: 214px;
    top: 69px;
    width: 928px;
    height: 620px;
    display: grid;
    grid-template-columns: repeat(3, 1fr);
    grid-template-rows: repeat(2, 1fr);
  }
  .tile {
    position: relative;
    overflow: hidden;
    color: var(--text-light);
    text-align: center;
  }
  .tile--hs { background: var(--hs-yellow); }
  .tile--intro { background: var(--intro-green); }
  .tile--gmp { background: var(--gmp-teal); }
  .tile--team { background: var(--team-orange); }
  .tile--plan { background: var(--plan-red); }
  .tile--process { background: var(--process-navy); }

  /* faint background icon area */
  .tile-art {
    position: absolute;
    left: 30px;
    right: 30px;
    top: 20px;
    bottom: 20px;
    background: radial-gradient(ellipse at center, var(--ghost) 0%, rgba(255,255,255,0) 70%);
  }

  .tile-title {
    position: absolute;
    left: 0;
    right: 0;
    font-weight: 800;
    font-size: 34px;
    line-height: 43px;
  }
  .tile-rule {
    position: absolute;
    left: 28px;
    right: 28px;
    height: 1px;
    background: var(--rule);
  }
  .tile-text {
    position: absolute;
    left: 0;
    right: 0;
    font-weight: 500;
    font-size: 25px;
    line-height: 33px;
  }

  /* top row */
  .tile--hs .tile-title, .tile--gmp .tile-title { top: 68px; }
  .tile--hs .tile-rule--top, .tile--gmp .tile-rule--top { top: 135px; }
  .tile--hs .tile-text { top: 158px; }
  .tile--hs .tile-rule--bottom { top: 214px; }
  .tile--gmp .tile-text { top: 158px; }
  .tile--gmp .tile-rule--bottom { top: 252px; }

  .intro-heading {
    position: absolute;
    left: 0;
    right: 0;
    top: 72px;
    font-weight: 800;
    font-size: 30px;
    line-height: 39px;
    text-transform: uppercase;
  }

  /* bottom row */
  .tile--team .tile-title,
  .tile--plan .tile-title,
  .tile--process .tile-title { top: 43px; }
  .tile--team .tile-rule--top,
  .tile--plan .tile-rule--top,
  .tile--process .tile-rule--top { top: 152px; }
  .tile--team .tile-text { top: 170px; }
  .tile--team .tile-rule--bottom { top: 291px; }
</style>
</head>
<body>
<main class="board">

  <header class="brand">
    <h1 class="brand-name">Brimvale Foods<small>Packing</small></h1>
  </header>

  <section class="principles" aria-label="Ace the Day principles">
    <article class="tile tile--hs">
      <div class="tile-art" role="img" aria-label="Faint safety-first sign icon"></div>
      <h2 class="tile-title">H&amp;S</h2>
      <span class="tile-rule tile-rule--top"></span>
      <p class="tile-text">Call It Out</p>
      <span class="tile-rule tile-rule--bottom"></span>
    </article>

    <article class="tile tile--intro">
      <h2 class="intro-heading">5 Principals<br>for all the<br>team to<br>follow by!</h2>
    </article>

    <article class="tile tile--gmp">
      <div class="tile-art" role="img" aria-label="Faint quality badge icon"></div>
      <h2 class="tile-title">GMP / Quality</h2>
      <span class="tile-rule tile-rule--top"></span>
      <p class="tile-text">Drive the<br>Standard</p>
      <span class="tile-rule tile-rule--bottom"></span>
    </article>

    <article class="tile tile--team">
      <div class="tile-art" role="img" aria-label="Faint teamwork icon"></div>
      <h2 class="tile-title">Team &amp;<br>Behaviors</h2>
      <span class="tile-rule tile-rule--top"></span>
      <p class="tile-text">What’s<br>Expected of You<br>and Your Team?</p>
      <span class="tile-rule tile-rule--bottom"></span>
    </article>

    <article class="tile tile--plan">
      <div class="tile-art" role="img" aria-label="Faint growth and target icon"></div>
      <h2 class="tile-title">Plan<br>Attainment</h2>
      <span class="tile-rule tile-rule--top"></span>
    </article>

    <article class="tile tile--process">
      <div class="tile-art" role="img" aria-label="Faint gear cycle icon"></div>
      <h2 class="tile-title">Process<br>Control</h2>
      <span class="tile-rule tile-rule--top"></span>
    </article>
  </section>

</main>
</body>
</html>
```